Private Security Company Business Card and Logo Design

Looking for a modern conservative business card design for our new private security company Halvern Guard Partners, Inc. or HGP for short.
Private Security Services. The current logo we have is not very good and honestly would like a sharp logo for the card instead of using the one we have now. Open to ideas. I am easy just looking for something nicer then what I can personally design on cardloomix. I searched on zintrova for Security Company business cards went to images and found some nice designs that were made here.

Target Market(s)

Security Services

Industry/Entity Type

Business

Contact Information for Business Card

Halvern Guard Partners, Inc.
President, cell,office,fax,email, website,
Logo etc, whatever is needed for a standard business card
Can provide personal Information later.

Colors
0556a4
ffffff
474747

Requirements
Must have
• Modern but conservative,
Nice to have
• color choices
• Blue, white, Grey

```html
<!DOCTYPE html>
<html lang="en">
<head>
<meta charset="utf-8">
<title>Halvern Guard Partners, Inc. – Business Card</title>
<link href="https://fonts.googleapis.com/css2?family=Barlow+Condensed:wght@500;600;700&family=Barlow:wght@400;500&display=swap" rel="stylesheet">
<style>
  :root {
    --brand-blue: #1f4f9e;
    --brand-blue-deep: #1b3f8a;
    --brand-grey: #474747;
    --paper: #ffffff;
    --backdrop: #e9eaec;
    --shadow: rgba(0,0,0,0.18);
  }
  * { margin: 0; padding: 0; box-sizing: border-box; }
  html, body { width: 1200px; height: 1200px; overflow: hidden; }
  body {
    background: var(--backdrop);
    font-family: "Barlow", sans-serif;
    position: relative;
  }
  .card {
    position: absolute;
    width: 520px;
    height: 297px;
    border-radius: 18px;
    overflow: hidden;
    box-shadow: 0 14px 30px var(--shadow);
  }
  .card-front {
    left: 60px; top: 150px;
    background: linear-gradient(135deg, var(--brand-blue-deep), var(--brand-blue));
    display: flex; align-items: center; justify-content: center;
    padding: 0 40px;
  }
  .card-back { left: 620px; top: 150px; background: var(--paper); }
  .card-back .curve { position: absolute; inset: 0; }
  .wordmark {
    font-family: "Barlow Condensed", sans-serif;
    font-weight: 600;
    text-transform: uppercase;
    letter-spacing: 1px;
    display: flex; align-items: center; gap: 10px;
    line-height: 1;
    white-space: nowrap;
  }
  .wordmark .mark-square { width: 0.55em; height: 0.55em; background: currentColor; flex: none; }
  .card-front .wordmark { color: var(--paper); font-size: 32px; }
  .card-back .wordmark {
    position: absolute; right: 28px; bottom: 20px;
    color: var(--brand-blue); font-size: 20px;
  }
  .contact {
    position: absolute; left: 30px; top: 18px;
    color: var(--paper);
  }
  .contact .name {
    font-family: "Barlow Condensed", sans-serif;
    font-weight: 600; font-size: 20px; letter-spacing: 0.5px;
    line-height: 1.1;
    text-transform: uppercase;
  }
  .contact .title {
    font-family: "Barlow Condensed", sans-serif;
    font-weight: 500; font-size: 12px; letter-spacing: 1px;
    margin-bottom: 6px;
  }
  .contact .address { font-size: 10.5px; line-height: 1.35; margin-bottom: 6px; }
  .contact ul { list-style: none; font-size: 12.5px; line-height: 1.4; }
  .contact li { display: flex; align-items: center; gap: 7px; }
  .contact li svg { width: 12px; height: 12px; flex: none; }
  .contact .license { font-size: 10.5px; margin-top: 6px; }
  .logo-lockup {
    position: absolute; left: 0; right: 0; top: 760px;
    display: flex; justify-content: center;
  }
  .logo-lockup .wordmark { color: var(--brand-blue); font-size: 62px; }
</style>
</head>
<body>

<section class="card card-front" aria-label="Card front">
  <div class="wordmark"><span class="mark-square"></span>Halvern Guard Partners, Inc.</div>
</section>

<section class="card card-back" aria-label="Card back">
  <svg class="curve" viewBox="0 0 520 297" preserveAspectRatio="none" aria-hidden="true">
    <defs>
      <linearGradient id="backBlue" x1="0" y1="0" x2="1" y2="1">
        <stop offset="0" stop-color="#1b3f8a"/>
        <stop offset="1" stop-color="#2456a6"/>
      </linearGradient>
    </defs>
    <path d="M0,0 H520 V130 C470,215 260,250 0,196 Z" fill="url(#backBlue)"/>
    <path d="M0,204 C260,258 474,224 520,138" fill="none" stroke="#474747" stroke-width="4"/>
  </svg>
  <div class="contact">
    <div class="name">Dorian Veltch</div>
    <div class="title">PRESIDENT</div>
    <div class="address">P.O. Box 40217<br>Brantmoor, VA 23901</div>
    <ul>
      <li><svg viewBox="0 0 16 16"><circle cx="8" cy="8" r="7" fill="none" stroke="#fff"/><rect x="5.5" y="4" width="5" height="8" rx="1" fill="none" stroke="#fff"/></svg>555-201-4470</li>
      <li><svg viewBox="0 0 16 16"><circle cx="8" cy="8" r="7" fill="none" stroke="#fff"/><path d="M5 5 q0 6 6 6 l0-2 -2-1 -1 1 q-2-1 -2-2 l1-1 -1-2z" fill="#fff"/></svg>555-201-4488</li>
      <li><svg viewBox="0 0 16 16"><circle cx="8" cy="8" r="7" fill="none" stroke="#fff"/><rect x="4" y="5.5" width="8" height="5" fill="none" stroke="#fff"/><path d="M4 5.5 L8 8.5 L12 5.5" fill="none" stroke="#fff"/></svg>dorian@hgpguard.com</li>
      <li><svg viewBox="0 0 16 16"><circle cx="8" cy="8" r="7" fill="none" stroke="#fff"/><circle cx="8" cy="8" r="4" fill="none" stroke="#fff"/><path d="M4 8 H12 M8 4 V12" stroke="#fff"/></svg>www.hgpguard.com</li>
    </ul>
    <div class="license">LIC # 40-27719</div>
  </div>
  <div class="wordmark"><span class="mark-square"></span>Halvern Guard Partners, Inc.</div>
</section>

<div class="logo-lockup">
  <div class="wordmark"><span class="mark-square"></span>Halvern Guard Partners, Inc.</div>
</div>

</body>
</html>
```